Fitness Centre/Personal Trainer Business Card

We need a business card design for a company based in Singapore called 'Vigor Lattice'.

We are a team of Personal Trainers and we are planning to open our new training facility.

This design will also be printed/painted on the walls in our gym.

We are a new breed of personal trainers who take fitness seriously and holistically. We do not merely train our clients to be big and muscular.

We believe in wholeness. In our opinion, fitness should include: strength, speed, flexibility, mobility, stamina & agility. These are what we train for. Of course, nutrition/diet is key.

We use fitness tools such as kettlebells, QLM, Pylometric boxes, battling ropes, clubbells, medicine balls, bulgarian bags etc - functional and non-bulky tools.

I currently have a Facebook page 'Vigor Lattice SG' which shows a logo of a kettlebell. But my business focus has since changed.

Services provided:
- Kettlebell Sport Preparation
- Calisthenics Training
- Corrective Exercises
- Sports Strength & Conditioning
- 28 days Weight Loss Program
- Myofascial Rehab Therapy
- Sports/Thai Massage

Main colors for the design should be BLACK & YELLOW. We envision a design which is able to protray the holistic view we take on fitness. Also it should somewhat appeal to the ladies and not intimidate them.

Target Market(s)

People between 18-35 years old. Students and working class alike.

Industry/Entity Type

Training

Requirements
Must have
• Name: Marcus Oriel Boon
Fitness Coach
Corrective Exercise Specialist
M: +65 9042 7736
E: marcus@sgvigorlattice.example

Double-sided please.
Nice to have
• "Where does your vigor lattice stand?"

```html
<!DOCTYPE html>
<html lang="en">
<head>
<meta charset="utf-8">
<title>Vigor Lattice Business Card</title>
<link rel="stylesheet" href="https://fonts.googleapis.com/css2?family=Saira:wght@800;900&family=Ubuntu:wght@400;500&display=swap">
<style>
  :root {
    --stage: #e6e6e6;
    --yellow-light: #e9ef1a;
    --yellow-mid: #cdd30f;
    --yellow-deep: #a9ad0c;
    --ink: #141414;
    --card-black: #1c1c1c;
    --paper: #ffffff;
    --muted: #e4e4e4;
  }
  * { box-sizing: border-box; margin: 0; padding: 0; }
  html, body { width: 1200px; height: 861px; overflow: hidden; }
  body {
    background: var(--stage);
    font-family: "Ubuntu", "Helvetica Neue", Arial, sans-serif;
    position: relative;
  }
  .card {
    position: absolute;
    top: 265px;
    width: 520px;
    height: 330px;
    border-radius: 18px;
    overflow: hidden;
  }
  .card--front {
    left: 45px;
    background: linear-gradient(160deg, var(--yellow-light) 0%, var(--yellow-mid) 55%, var(--yellow-deep) 100%);
    color: var(--ink);
    text-align: center;
    padding-top: 40px;
  }
  .tagline-lead {
    font-family: "Saira", "Arial Black", sans-serif;
    font-weight: 800;
    font-size: 30px;
    line-height: 1;
    color: #262626;
  }
  .tagline-name {
    font-family: "Saira", "Arial Black", sans-serif;
    font-weight: 900;
    font-size: 50px;
    line-height: 0.95;
    letter-spacing: -1px;
    margin-top: 12px;
    text-transform: uppercase;
  }
  .services {
    margin-top: 24px;
    font-size: 14px;
    line-height: 1.35;
    color: #1e1e1e;
  }
  .services .dot { font-size: 10px; vertical-align: 2px; padding: 0 3px; }

  .card--back {
    left: 635px;
    background: var(--card-black);
    color: var(--paper);
  }
  .back-feature {
    position: absolute;
    inset: 0;
    background: linear-gradient(170deg, #eef21c 0%, #c9ce10 36%, var(--card-black) 47%);
  }
  .brand-name {
    position: absolute;
    left: 34px;
    top: 28px;
    font-family: "Saira", "Arial Black", sans-serif;
    font-weight: 900;
    font-size: 48px;
    line-height: 0.9;
    color: var(--ink);
    text-transform: uppercase;
    letter-spacing: -1px;
  }
  .holder { position: absolute; left: 40px; top: 205px; }
  .holder-name { font-size: 28px; font-weight: 500; letter-spacing: 0.5px; }
  .holder-role { font-size: 16px; font-weight: 500; color: var(--muted); margin-top: 6px; }
  .contacts {
    position: absolute;
    left: 40px;
    top: 283px;
    display: flex;
    gap: 26px;
    font-size: 16px;
    color: var(--muted);
  }
  .contact { display: flex; align-items: center; gap: 8px; }
  .contact svg { width: 22px; height: 22px; flex: none; }
</style>
</head>
<body>

<section class="card card--front" aria-label="Card front">
  <p class="tagline-lead">Where does your</p>
  <p class="tagline-name">Vigor<br>Lattice stand?</p>
  <p class="services">
    Kettlebell Sport Preparation <span class="dot">●</span> Calisthenics Training<br>
    Corrective Exercises <span class="dot">●</span> Sports Strength &amp; Conditioning<br>
    28 days Weight Loss Program <span class="dot">●</span> Myofascial Rehab Therapy<br>
    Sports/Thai Massage
  </p>
</section>

<section class="card card--back" aria-label="Card back">
  <div class="back-feature" role="img" aria-label="Yellow and black torn paper graphic across the upper card"></div>

  <p class="brand-name">Vigor<br>Lattice</p>

  <div class="holder">
    <p class="holder-name">Marcus Oriel Boon</p>
    <p class="holder-role">Fitness Coach/ Corrective Exercise Specialist</p>
  </div>

  <div class="contacts">
    <p class="contact">
      <svg viewBox="0 0 22 22" aria-hidden="true">
        <circle cx="11" cy="11" r="11" fill="#e4e4e4"/>
        <rect x="9" y="4.5" width="4.5" height="13" rx="1.2" fill="#1c1c1c" transform="rotate(40 11 11)"/>
      </svg>
      +65 9042 7736
    </p>
    <p class="contact">
      <svg viewBox="0 0 22 22" aria-hidden="true">
        <circle cx="11" cy="11" r="11" fill="#e4e4e4"/>
        <rect x="5" y="7" width="12" height="8.5" rx="1" fill="#1c1c1c"/>
        <polyline points="5.5,7.5 11,12 16.5,7.5" fill="none" stroke="#e4e4e4" stroke-width="1.2"/>
      </svg>
      marcus@sgvigorlattice.example
    </p>
  </div>
</section>

</body>
</html>
```